Small business updating business cards

We have already updated our logo via Pixel Forge and downloaded it (hopefully) for you to use. Now an updated set of business cards for Owen Brennan and Stuart Brennan are also needed... we are also hoping that a copy of our outdated business card designs have uploaded successfully as Microsoft Publisher files. Our Strength Through Unity motto has died a slow death so we are hoping to remove it (and other superfluous lingo if the graphic covers the idea) and instead opt for a fancy graphic (?) on the second side of the card that really reflects our desire to obtain product / haulage from Road Transport / Yard Operators and convert legs of their haulage to rail freight where profitable (bulk haulage / containterised etc). Can you help us look larger, bolder and more robust than we really are (two man show)?
Target Market(s)
Transport Industry
Industry/Entity Type
Business
Contact Information for Business Card
Card details for both O Brennan and S Brennan have been uploaded on the publisher files
Colors
Designer to choose colors to be used in the design.
Requirements
Must have
- Similar theme both sides of card
Should not have
- Black on one side white on the other

```html
<!DOCTYPE html>
<html lang="en">
<head>
<meta charset="utf-8">
<title>Norlink Freight – Business Cards</title>
<link rel="stylesheet" href="https://fonts.googleapis.com/css2?family=Open+Sans:wght@400;600;700;800&display=swap">
<style>
  :root {
    --bg: #e4ecc4;
    --card: #f7f7f5;
    --gold: #9a8530;
    --teal: #137f9b;
    --teal-dark: #0e6f88;
    --cyan: #17b3e3;
    --white: #ffffff;
    --ink: #1d5f72;
  }
  * { box-sizing: border-box; margin: 0; padding: 0; }
  html, body { width: 1200px; height: 835px; overflow: hidden; background: var(--bg); }
  body { position: relative; font-family: "Open Sans", Arial, sans-serif; }

  .card {
    position: absolute;
    top: 255px;
    width: 540px;
    height: 320px;
    background: var(--card);
    box-shadow: 0 10px 26px rgba(60, 80, 20, 0.22);
    overflow: hidden;
  }

  /* Front */
  .card--front { left: 40px; }
  .front-frame { position: absolute; inset: 0; }
  .front-brand {
    position: absolute;
    left: 0; right: 0; top: 118px;
    text-align: center;
    font-weight: 800;
    font-size: 54px;
    letter-spacing: -0.5px;
    color: var(--teal);
  }
  .front-rule {
    position: absolute;
    top: 200px;
    height: 2px;
    background: var(--teal);
  }
  .front-rule--left { left: 70px; width: 150px; }
  .front-rule--right { right: 70px; width: 150px; }
  .front-dot {
    position: absolute;
    left: 262px; top: 195px;
    width: 12px; height: 12px;
    background: var(--teal);
    border-radius: 50%;
  }

  /* Back */
  .card--back { left: 620px; }
  .back-edge { position: absolute; left: 0; top: 0; width: 6px; height: 100%; background: var(--teal); }
  .back-brand-block {
    position: absolute;
    left: 22px; top: 92px;
    width: 250px;
    text-align: center;
  }
  .back-brand {
    font-weight: 800;
    font-size: 30px;
    color: var(--teal);
    letter-spacing: -0.3px;
  }
  .back-brand-rule { display: block; height: 2px; width: 190px; margin: 8px auto 14px; background: var(--teal); }
  .back-strapline {
    font-weight: 700;
    font-size: 13.5px;
    line-height: 1.35;
    color: var(--teal);
    text-transform: uppercase;
    letter-spacing: 0.3px;
  }

  .back-panel {
    position: absolute;
    right: 0; top: 0;
    width: 250px; height: 100%;
    background: var(--teal);
  }
  .name-ribbon { position: absolute; left: 262px; top: 34px; width: 278px; height: 96px; }
  .name-block { position: absolute; left: 300px; top: 48px; color: var(--white); }
  .person-name { font-weight: 700; font-size: 30px; letter-spacing: 0.5px; line-height: 1; }
  .person-role { font-size: 16px; font-style: normal; opacity: 0.95; margin-top: 2px; color: var(--teal-dark); }

  .contact-list {
    position: absolute;
    left: 298px; top: 148px;
    list-style: none;
    color: var(--white);
    font-size: 13.5px;
    line-height: 1.4;
  }
  .contact-item { display: flex; gap: 10px; margin-bottom: 6px; }
  .contact-icon { width: 14px; height: 14px; flex: none; margin-top: 3px; }
</style>
</head>
<body>

<section class="card card--front" aria-label="Business card front">
  <svg class="front-frame" width="540" height="320" viewBox="0 0 540 320" aria-hidden="true">
    <g fill="none" stroke="var(--gold)" stroke-width="1.6">
      <path d="M22 46 V22 H60 M480 22 H518 V46 M518 274 V298 H480 M60 298 H22 V274"/>
      <rect x="34" y="34" width="472" height="252"/>
    </g>
  </svg>
  <div class="front-brand">Norlink Freight</div>
  <span class="front-rule front-rule--left"></span>
  <span class="front-dot"></span>
  <span class="front-rule front-rule--right"></span>
</section>

<section class="card card--back" aria-label="Business card back">
  <span class="back-edge"></span>
  <div class="back-brand-block">
    <div class="back-brand">Norlink Freight</div>
    <span class="back-brand-rule"></span>
    <p class="back-strapline">Strategic alliance partner<br>providing logistical freight<br>solutions</p>
  </div>

  <div class="back-panel"></div>
  <svg class="name-ribbon" viewBox="0 0 278 96" aria-hidden="true">
    <polygon points="0,12 278,0 278,78 0,78" fill="var(--cyan)"/>
    <polygon points="0,78 28,78 28,96" fill="var(--teal-dark)"/>
  </svg>
  <div class="name-block">
    <div class="person-name">OWEN BRENNAN</div>
    <div class="person-role">Director</div>
  </div>

  <ul class="contact-list">
    <li class="contact-item">
      <svg class="contact-icon" viewBox="0 0 14 14"><circle cx="7" cy="7" r="6" fill="none" stroke="#fff" stroke-width="1.3"/><path d="M5 4 L6.5 4 L7 6 L6 6.8 Q6.8 8 8 8.6 L8.8 7.6 L10.5 8.2 L10.3 9.8 Q6 10 4.5 5.2 Z" fill="#fff"/></svg>
      <span>0400 318 762</span>
    </li>
    <li class="contact-item">
      <svg class="contact-icon" viewBox="0 0 14 14"><rect x="1" y="3" width="12" height="8" fill="#fff"/><path d="M1 3 L7 8 L13 3" fill="none" stroke="var(--teal)" stroke-width="1.2"/></svg>
      <span>brennano@norlinkfreight.com.au<br>norlinkfreight@mailbox.com<br>norlinkfreight@postbox.com</span>
    </li>
    <li class="contact-item">
      <svg class="contact-icon" viewBox="0 0 14 14"><circle cx="7" cy="7" r="6" fill="none" stroke="#fff" stroke-width="1.3"/><path d="M1 7 H13 M7 1 Q3 7 7 13 Q11 7 7 1" fill="none" stroke="#fff" stroke-width="1"/></svg>
      <span>www.norlinkfreight.com.au</span>
    </li>
    <li class="contact-item">
      <svg class="contact-icon" viewBox="0 0 14 14"><path d="M7 13 Q2 7 2 5 A5 5 0 0 1 12 5 Q12 7 7 13 Z" fill="#fff"/><circle cx="7" cy="5" r="1.8" fill="var(--teal)"/></svg>
      <span>22 Marlow Crescent Fennel Bay<br>NSW 2284</span>
    </li>
  </ul>
</section>

</body>
</html>
```